Investor Deck

We have an existing presentation that needs to be polished and made professional and graphically state of the art.

Attaching, Corporate Power Point Template it says Company
Draft with content - has content

We need this to look professional for the ceo to present to investors.
Additional images that can be incorporated - samples of posters that are pirnted at this location.

```html
<!DOCTYPE html>
<html lang="en">
<head>
<meta charset="utf-8">
<title>Company Presentation Template</title>
<link href="https://fonts.googleapis.com/css2?family=Roboto:wght@400;500;700;900&family=Roboto+Condensed:wght@700&display=swap" rel="stylesheet">
<style>
:root{
  --blue:#0aa9dc;
  --blue-deep:#0b86bf;
  --navy:#1c3a78;
  --orange:#f7901e;
  --peach:#f9c48e;
  --ink:#444;
  --muted:#777;
  --board:#777a7e;
  --pale:#dcecf7;
  --paler:#eef5fb;
}
*{margin:0;padding:0;box-sizing:border-box}
html,body{width:1200px;height:944px;overflow:hidden;background:var(--board);font-family:"Roboto",sans-serif;color:var(--ink)}
.board{position:relative;width:1200px;height:944px}
.slide{position:absolute;width:370px;height:208px;background:#fff;overflow:hidden;box-shadow:0 2px 6px rgba(0,0,0,.35)}
.abs{position:absolute}
.title{position:absolute;left:13px;top:12px;font-family:"Roboto Condensed",sans-serif;font-weight:700;font-size:13px;color:var(--navy);letter-spacing:.2px}
.title::after{content:"";position:absolute;left:0;top:19px;width:20px;height:1.5px;background:var(--orange)}
.brand{position:absolute;right:10px;top:10px;display:flex;align-items:center;gap:3px}
.brand .mark{width:5px;height:5px;background:var(--orange)}
.brand .name{font-size:6.5px;font-weight:500;color:var(--navy)}
.brand .tag{position:absolute;right:0;top:9px;font-size:2.4px;color:var(--muted);white-space:nowrap}
.brand.light .name{color:#fff}
.brand.light .tag{color:#e8f6fc}
.footer{position:absolute;left:11px;right:11px;bottom:9px;display:flex;align-items:center;gap:3px;font-size:4.5px;color:var(--ink)}
.footer .rule{flex:1;height:.5px;background:var(--orange)}
.footer.light{color:#fff}
.txt{position:absolute;font-size:3.8px;line-height:1.5;color:var(--ink)}
.txt.white{color:#fff}
.photo{position:absolute}
.num{position:absolute;width:16px;height:16px;background:var(--orange);color:#fff;font-weight:900;font-size:12px;line-height:16px;text-align:center}
.num.sm{width:10px;height:10px;font-size:8px;line-height:10px}
.item-h{position:absolute;font-size:8px;font-weight:500;color:var(--navy)}
.item-h.sm{font-size:5px}
.item-p{position:absolute;font-size:4px;line-height:1.4;color:#fff}
.item-p.dark{color:var(--muted);font-size:2.8px}
.month{position:absolute;width:22px;text-align:center;font-weight:700;font-size:8px;color:var(--blue)}
.mnum{position:absolute;font-size:6px;color:var(--orange)}
.mtext{position:absolute;width:28px;font-size:2.4px;line-height:1.35;color:var(--muted)}
.phone{position:absolute;width:46px;height:98px;border:1.5px solid #222;border-radius:4px;background:#fff}
.phone h5{font-size:5.5px;font-weight:400;color:var(--navy);margin:20px 4px 0}
.phone p{font-size:2.4px;line-height:1.35;color:var(--muted);margin:6px 4px 0}
.tile{position:absolute;width:74px}
.tile .img{height:50px;border:1.5px solid var(--peach)}
.tile h6{font-size:5.5px;font-weight:500;color:#fff;margin-top:3px}
.tile p{font-size:2.6px;line-height:1.35;color:#fff}
.bullets{position:absolute;list-style:none;font-size:7px;color:#555;line-height:14.3px}
.bullets li::before{content:"";display:inline-block;width:2.5px;height:2.5px;background:var(--orange);margin-right:5px;vertical-align:middle}
.info p{font-size:4px;line-height:1.4;color:#fff;margin-bottom:8px}
.info b{font-weight:700}
.table{position:absolute;left:125px;top:53px;width:223px;border-collapse:collapse;table-layout:fixed}
.table td{width:33.33%;height:22px;border-right:1px solid #fff;font-size:5.5px;font-weight:700;color:#fff;padding:0 3px;vertical-align:middle}
.table tr:nth-child(1) td{background:var(--blue)}
.table tr:nth-child(even) td{background:var(--pale)}
.table tr:nth-child(odd):not(:first-child) td{background:var(--paler)}
.avatar{position:absolute;width:34px;height:34px;border-radius:50%;border:2px solid var(--orange);background:radial-gradient(circle at 50% 45%,#d9d2cc,#9aa7b1)}
.person{position:absolute;width:60px;text-align:center}
.person h6{font-size:7px;font-weight:700;color:var(--orange)}
.person p{font-size:2.6px;line-height:1.35;color:var(--muted);margin-top:2px}
</style>
</head>
<body>
<main class="board">

<!-- 01 Cover -->
<section class="slide" style="left:31px;top:31px">
  <div class="abs" style="left:0;top:0;width:16px;height:16px;background:var(--peach)"></div>
  <div class="abs" style="left:16px;top:16px;width:16px;height:16px;background:#eee"></div>
  <div class="abs" style="left:176px;top:0;width:194px;height:208px;background:var(--blue)"></div>
  <div class="photo" role="img" aria-label="Team celebrating with high fives in a bright office" style="left:176px;top:10px;width:178px;height:188px;background:linear-gradient(160deg,#e8ecef,#b9c3cb 55%,#8c9aa6)"></div>
  <div class="abs" style="left:176px;top:10px;width:12px;height:12px;background:var(--orange)"></div>
  <div class="abs" style="left:188px;top:22px;width:12px;height:12px;background:var(--navy)"></div>
  <div class="abs" style="left:42px;top:39px;display:flex;align-items:center;gap:4px">
    <span style="width:8px;height:8px;background:var(--orange)"></span>
    <span style="font-size:10px;font-weight:500;color:var(--navy)">StatuteWorks</span>
  </div>
  <div class="abs" style="left:54px;top:52px;font-size:3.2px;color:var(--muted)">Workplace Policy Advisors</div>
  <div class="abs" style="left:20px;top:88px;width:1.5px;height:57px;background:var(--blue)"></div>
  <div class="abs" style="left:29px;top:92px;font-size:11px;color:var(--orange)">COMPANY</div>
  <div class="abs" style="left:29px;top:104px;font-size:20px;font-weight:900;color:var(--navy)">POWERPOINT</div>
  <div class="abs" style="left:29px;top:127px;font-size:13px;font-weight:500;color:var(--blue)">PRESENTATION</div>
  <div class="abs" style="left:30px;top:159px;font-size:6px;font-family:serif;font-weight:700;color:#555">Name:</div>
  <div class="abs" style="left:30px;top:177px;font-size:6px;font-family:serif;font-weight:700;color:#555">Date:</div>
  <div class="abs" style="left:141px;top:185px;width:12px;height:12px;background:var(--peach)"></div>
  <div class="abs" style="left:153px;top:197px;width:12px;height:11px;background:#eee"></div>
</section>

<!-- 02 Agenda -->
<section class="slide" style="left:415px;top:31px">
  <div class="abs" style="left:0;top:0;width:271px;height:208px;background:var(--blue)"></div>
  <div class="abs" style="left:271px;top:31px;width:99px;height:177px;background:var(--blue)"></div>
  <div class="title">AGENDA</div>
  <div class="brand"><span class="mark"></span><span class="name">StatuteWorks</span><span class="tag">Workplace Policy Advisors</span></div>
  <div class="abs" style="left:191px;top:33px;width:148px;height:148px;border-radius:50%;border:3px solid var(--orange);background:#fff"></div>
  <div class="photo" role="img" aria-label="Two colleagues smiling at a laptop" style="left:197px;top:39px;width:136px;height:136px;border-radius:50%;background:linear-gradient(150deg,#f1f3f5,#c7ced4 60%,#8d969e)"></div>
  <div class="num" style="left:21px;top:55px">1.</div>
  <div class="item-h" style="left:48px;top:53px">Lorem ipsum</div>
  <div class="item-p" style="left:48px;top:66px">Lorem ipsum dolor sit amet, consectetuer<br>adipiscing elit, sed diam nonummy nibh</div>
  <div class="num" style="left:21px;top:97px">2.</div>
  <div class="item-h" style="left:48px;top:95px">Lorem ipsum</div>
  <div class="item-p" style="left:48px;top:108px">Lorem ipsum dolor sit amet, consectetuer<br>adipiscing elit, sed diam nonummy nibh</div>
  <div class="num" style="left:21px;top:138px">3.</div>
  <div class="item-h" style="left:48px;top:136px">Lorem ipsum</div>
  <div class="item-p" style="left:48px;top:149px">Lorem ipsum dolor sit amet, consectetuer<br>adipiscing elit, sed diam nonummy nibh</div>
  <div class="footer light"><span>10/10/2023</span><span class="rule"></span><span>02</span></div>
</section>

<!-- 03 Text here with icons -->
<section class="slide" style="left:799px;top:31px">
  <div class="title">TEXT HERE</div>
  <div class="brand"><span class="mark"></span><span class="name">StatuteWorks</span><span class="tag">Workplace Policy Advisors</span></div>
  <p class="txt" style="left:13px;top:37px;width:345px">Lorem ipsum dolor sit amet, consectetuer adipiscing elit, sed diam nonummy nibh euismod tincidunt ut laoreet dolore magna aliquam erat volutpat. Ut wisi enim ad minim veniam, quis nostrud exerci tation ullamcorper suscipit lobortis nisl ut aliquip ex ea commodo consequat. Duis autem vel eum iriure dolor in hendrerit in vulputate velit esse molestie consequat, vel illum dolore eu feugiat nulla facilisis at vero eros et accumsan et iusto odio dignissim qui blandit praesent luptatum zzril delenit augue duis dolore te feugait nulla facilisi.</p>
  <p class="txt" style="left:13px;top:70px;width:345px">Lorem ipsum dolor sit amet, cons ectetuer adipiscing elit, sed diam nonummy nibh euismod tincidunt ut laoreet dolore magna aliquam erat volutpat. Ut wisi enim ad minim veniam, quis nostrud exerci tation ullamcorper suscipit lobortis nisl ut aliquip ex ea commodo consequat.</p>
  <div class="photo" role="img" aria-label="Office team at work tinted blue" style="left:0;top:107px;width:370px;height:76px;background:linear-gradient(90deg,#0d9fd3,#12aee0 50%,#0d9fd3)"></div>
  <svg class="abs" style="left:0;top:90px" width="370" height="95" viewBox="0 0 370 95">
    <g fill="#fff" stroke="var(--blue-deep)" stroke-width="1">
      <circle cx="68" cy="19" r="17"/><circle cx="178" cy="19" r="17"/><circle cx="288" cy="19" r="17"/>
    </g>
    <g fill="none" stroke="var(--navy)" stroke-width="1.2">
      <rect x="61" y="12" width="14" height="10"/><path d="M63 20l3-3 3 2 4-5"/>
      <rect x="171" y="13" width="14" height="11"/><circle cx="175" cy="19" r="2"/>
      <path d="M281 26v-6M286 26v-9M291 26v-12M279 27h16"/>
    </g>
    <g fill="var(--orange)"><circle cx="62" cy="26" r="1.5"/><rect x="180" y="9" width="6" height="4"/></g>
    <g font-family="Roboto,sans-serif" fill="#fff" text-anchor="middle">
      <text x="68" y="52" font-size="7" font-weight="700">LOREM IPSUM</text>
      <text x="178" y="52" font-size="7" font-weight="700">LOREM IPSUM</text>
      <text x="288" y="52" font-size="7" font-weight="700">LOREM IPSUM</text>
      <g font-size="4.6">
        <text x="68" y="59">Lorem ipsum dolor sit amet,</text><text x="68" y="66">consectetuer adipiscing elit,</text><text x="68" y="73">sed diam nonummy nibh</text><text x="68" y="80">euismod tincid</text>
        <text x="178" y="59">Lorem ipsum dolor sit amet,</text><text x="178" y="66">consectetuer adipiscing elit,</text><text x="178" y="73">sed diam nonummy nibh</text><text x="178" y="80">euismod tincid</text>
        <text x="288" y="59">Lorem ipsum dolor sit amet,</text><text x="288" y="66">consectetuer adipiscing elit,</text><text x="288" y="73">sed diam nonummy nibh</text><text x="288" y="80">euismod tincid</text>
      </g>
    </g>
  </svg>
  <div class="footer"><span>10/10/2023</span><span class="rule"></span><span>03</span></div>
</section>

<!-- 04 Month highlights -->
<section class="slide" style="left:31px;top:258px">
  <div class="abs" style="left:0;top:0;width:114px;height:4px;background:var(--blue)"></div>
  <div class="abs" style="left:0;top:0;width:4px;height:208px;background:var(--blue)"></div>
  <div class="abs" style="left:0;top:204px;width:114px;height:4px;background:var(--blue)"></div>
  <div class="abs" style="left:256px;top:204px;width:114px;height:4px;background:var(--blue)"></div>
  <div class="abs" style="left:366px;top:0;width:4px;height:208px;background:var(--blue)"></div>
  <div class="title">[MONTH] HIGHLIGHTS</div>
  <div class="brand" style="right:12px"><span class="mark"></span><span class="name">StatuteWorks</span><span class="tag">Workplace Policy Advisors</span></div>
  <svg class="abs" style="left:0;top:0" width="370" height="208" viewBox="0 0 370 208">
    <path d="M47 86H66M70 86H280a23.5 23.5 0 0 1 0 47H68M63 133H58" fill="none" stroke="var(--navy)" stroke-width="1"/>
    <g fill="var(--blue)" stroke="var(--navy)" stroke-width=".8">
      <circle cx="82" cy="86" r="2.5"/><circle cx="119" cy="86" r="2.5"/><circle cx="156" cy="86" r="2.5"/><circle cx="193" cy="86" r="2.5"/><circle cx="229" cy="86" r="2.5"/><circle cx="266" cy="86" r="2.5"/>
      <circle cx="82" cy="133" r="2.5"/><circle cx="119" cy="133" r="2.5"/><circle cx="156" cy="133" r="2.5"/><circle cx="193" cy="133" r="2.5"/><circle cx="229" cy="133" r="2.5"/><circle cx="266" cy="133" r="2.5"/>
    </g>
  </svg>
  <div class="month" style="left:71px;top:91px">Jan</div><div class="month" style="left:108px;top:91px">Feb</div><div class="month" style="left:145px;top:91px">Mar</div><div class="month" style="left:182px;top:91px">Apr</div><div class="month" style="left:218px;top:91px">May</div><div class="month" style="left:255px;top:91px">Jun</div>
  <div class="month" style="left:71px;top:118px">Dec</div><div class="month" style="left:108px;top:118px">Nov</div><div class="month" style="left:145px;top:118px">Oct</div><div class="month" style="left:182px;top:118px">Sep</div><div class="month" style="left:218px;top:118px">Aug</div><div class="month" style="left:255px;top:118px">Jul</div>
  <div class="mnum" style="left:68px;top:47px">01</div><div class="mnum" style="left:105px;top:47px">02</div><div class="mnum" style="left:142px;top:47px">03</div><div class="mnum" style="left:179px;top:47px">04</div><div class="mnum" style="left:216px;top:47px">05</div><div class="mnum" style="left:253px;top:47px">06</div>
  <div class="mtext" style="left:68px;top:56px">Lorem ipsum dolor sit amet, consectetuer adipiscing elit, sed diam nonummy nibh</div>
  <div class="mtext" style="left:105px;top:56px">Lorem ipsum dolor sit amet, consectetuer adipiscing elit, sed</div>
  <div class="mtext" style="left:142px;top:56px">Lorem ipsum dolor sit amet, consectetuer adipiscing elit, sed</div>
  <div class="mtext" style="left:179px;top:56px">Lorem ipsum dolor sit amet, consectetuer adipiscing elit, sed diam nonummy nibh</div>
  <div class="mtext" style="left:216px;top:56px">Lorem ipsum dolor sit amet, consectetuer adipiscing elit, sed</div>
  <div class="mtext" style="left:253px;top:56px">Lorem ipsum dolor sit amet, consectetuer adipiscing elit, sed</div>
  <div class="mnum" style="left:68px;top:147px">12</div><div class="mnum" style="left:105px;top:147px">11</div><div class="mnum" style="left:142px;top:147px">10</div><div class="mnum" style="left:179px;top:147px">09</div><div class="mnum" style="left:216px;top:147px">08</div><div class="mnum" style="left:253px;top:147px">07</div>
  <div class="mtext" style="left:68px;top:156px">Lorem ipsum dolor sit amet, consectetuer adipiscing elit, sed diam nonummy nibh</div>
  <div class="mtext" style="left:105px;top:156px">Lorem ipsum dolor sit amet, consectetuer adipiscing elit, sed diam nonummy nibh</div>
  <div class="mtext" style="left:142px;top:156px">Lorem ipsum dolor sit amet, consectetuer adipiscing elit, sed diam nonummy nibh</div>
  <div class="mtext" style="left:179px;top:156px">Lorem ipsum dolor sit amet, consectetuer adipiscing elit, sed diam nonummy nibh</div>
  <div class="mtext" style="left:216px;top:156px">Lorem ipsum dolor sit amet, consectetuer adipiscing elit, sed diam nonummy nibh</div>
  <div class="mtext" style="left:253px;top:156px">Lorem ipsum dolor sit amet, consectetuer adipiscing elit, sed diam nonummy nibh</div>
  <div class="footer"><span>10/10/2023</span><span class="rule"></span><span>04</span></div>
</section>

<!-- 05 Statistics -->
<section class="slide" style="left:415px;top:258px">
  <div class="abs" style="left:0;top:0;width:114px;height:4px;background:var(--blue)"></div>
  <div class="abs" style="left:366px;top:95px;width:4px;height:113px;background:var(--blue)"></div>
  <div class="title" style="top:14px">STATISTICS</div>
  <div class="brand"><span class="mark"></span><span class="name">StatuteWorks</span><span class="tag">Workplace Policy Advisors</span></div>
  <p class="txt" style="left:16px;top:37px;width:300px">Lorem ipsum dolor sit amet, consectetuer adipiscing elit, sed diam nonummy nibh euismod tincidunt ut laoreet dolore magna aliquam erat volutpat. Ut wisi enim ad minim veniam, quis nostrud exerci tation ullamcorper suscipit lobortis nisl ut aliquip ex ea commodo consequat. Duis autem vel eum iriure dolor in hendrerit i</p>
  <svg class="abs" style="left:16px;top:71px" width="175" height="109" viewBox="0 0 175 109">
    <rect x=".5" y=".5" width="174" height="108" fill="#fff" stroke="#ddd"/>
    <text x="87" y="8" font-size="4.8" text-anchor="middle" fill="#555" font-family="Roboto,sans-serif">Company Growth</text>
    <g font-size="3" fill="#666" font-family="Roboto,sans-serif">
      <text x="4" y="15">6</text><text x="4" y="28">5</text><text x="4" y="40">4</text><text x="4" y="52">3</text><text x="4" y="64">2</text><text x="4" y="76">1</text><text x="4" y="88">0</text>
      <text x="20" y="95">Category 1</text><text x="60" y="95">Category 2</text><text x="100" y="95">Category 3</text><text x="140" y="95">Category 4</text>
      <text x="66" y="103">Series 1</text><text x="85" y="103">Series 2</text><text x="104" y="103">Series 3</text>
    </g>
    <line x1="10" y1="87" x2="170" y2="87" stroke="#ccc" stroke-width=".5"/>
    <g fill="var(--blue)"><rect x="17" y="35" width="6" height="52"/><rect x="57" y="58" width="6" height="29"/><rect x="97" y="44" width="6" height="43"/><rect x="137" y="32" width="6" height="55"/></g>
    <g fill="var(--orange)"><rect x="24" y="58" width="6" height="29"/><rect x="64" y="33" width="6" height="54"/><rect x="104" y="65" width="6" height="22"/><rect x="144" y="54" width="6" height="33"/></g>
    <g fill="var(--navy)"><rect x="31" y="63" width="6" height="24"/><rect x="71" y="63" width="6" height="24"/><rect x="111" y="50" width="6" height="37"/><rect x="151" y="26" width="6" height="61"/></g>
    <rect x="62" y="100.5" width="2.5" height="2.5" fill="var(--blue)"/><rect x="81" y="100.5" width="2.5" height="2.5" fill="var(--orange)"/><rect x="100" y="100.5" width="2.5" height="2.5" fill="var(--navy)"/>
  </svg>
  <svg class="abs" style="left:210px;top:72px" width="126" height="76" viewBox="0 0 126 76">
    <ellipse cx="63" cy="42" rx="60" ry="30" fill="#0a7fb0"/>
    <path d="M63 12a60 30 0 0 0-60 30 60 30 0 0 0 52 29.5L58 48a24 10 0 0 1 5-18z" fill="var(--blue)"/>
    <path d="M63 12v18a24 10 0 0 1 22 4l34-8A60 30 0 0 0 63 12z" fill="var(--orange)"/>
    <path d="M119 26l-34 8a24 10 0 0 1 2 12l36 0A60 30 0 0 0 119 26z" fill="var(--navy)"/>
    <path d="M123 46H87a24 10 0 0 1-29 2l-3 23A60 30 0 0 0 123 46z" fill="var(--orange)"/>
    <ellipse cx="68" cy="39" rx="22" ry="8" fill="#fff"/>
    <g fill="#fff" font-family="Roboto,sans-serif" font-weight="900" font-size="9">
      <text x="14" y="45">40%</text><text x="65" y="22">20%</text><text x="98" y="38">20%</text><text x="73" y="62">20%</text>
    </g>
  </svg>
  <div class="abs" style="left:198px;top:158px;font-size:6px;color:var(--blue)">● Lorem ipsum</div>
  <div class="txt" style="left:204px;top:166px;width:70px;font-size:2.8px;line-height:1.35">Lorem ipsum dolor sit amet, consectetuer adipiscing elit, sed diam nonummy nibh euismod tincidunt ut laoreet</div>
  <div class="abs" style="left:285px;top:158px;font-size:6px;color:var(--orange)">● Lorem ipsum</div>
  <div class="txt" style="left:292px;top:166px;width:70px;font-size:2.8px;line-height:1.35">Lorem ipsum dolor sit amet, consectetuer adipiscing elit, sed diam nonummy nibh euismod tincidunt ut laoreet</div>
  <div class="footer"><span>10/10/2023</span><span class="rule"></span><span>05</span></div>
</section>

<!-- 06 Strategic initiatives -->
<section class="slide" style="left:799px;top:258px">
  <div class="abs" style="left:0;top:0;width:258px;height:208px;background:var(--blue)"></div>
  <div class="title" style="top:13px">STRATEGIC INITIATIVES</div>
  <div class="brand"><span class="mark"></span><span class="name">StatuteWorks</span><span class="tag">Workplace Policy Advisors</span></div>
  <p class="txt white" style="left:15px;top:41px;width:188px;font-size:4.6px;line-height:1.3">Lorem ipsum dolor sit amet, consectetuer adipiscing elit, sed diam nonummy nibh euismod tincidunt ut laoreet dolore magna aliquam erat volutpat. Ut wisi enim ad minim veniam, quis nostrud exerci tation ullamcorper suscipit lobortis nisl ut aliquip ex ea commodo consequat. Duis autem vel eum iriure dolor in hendrerit in vulputate velit esse</p>
  <p class="txt white" style="left:15px;top:84px;width:188px;font-size:4.6px;line-height:1.3">Lorem ipsum dolor sit amet, consectetuer adipiscing elit, sed diam nonummy nibh euismod tincidunt ut laoreet dolore magna aliquam erat volutpat. Ut wisi enim ad minim veniam, quis nostrud exerci tation ullamcorper suscipit lobortis nisl ut aliquip ex ea commodo consequat. Duis autem vel eum iriure dolor in hendrerit in vulputate velit esse</p>
  <svg class="abs" style="left:19px;top:134px" width="8" height="30" viewBox="0 0 8 30"><path d="M1 1l5 3-5 3z" fill="var(--orange)"/><path d="M1 23l5 3-5 3z" fill="none" stroke="var(--navy)" stroke-width=".7"/></svg>
  <p class="txt white" style="left:32px;top:133px;width:172px;font-size:4.6px;line-height:1.3">Lorem ipsum dolor sit amet, consectetuer adipiscing elit, sed diam nonummy nibh euismod tincidunt ut laoreet dolore magna</p>
  <p class="txt white" style="left:32px;top:158px;width:172px;font-size:4.6px;line-height:1.3">Lorem ipsum dolor sit amet, consectetuer adipiscing elit, sed diam nonummy nibh euismod tincidunt ut laoreet dolore magna</p>
  <div class="abs" style="left:205px;top:35px;width:141px;height:141px;border:1px solid var(--orange);background:#fff"></div>
  <div class="photo" role="img" aria-label="Open-plan office with people working at desks" style="left:210px;top:40px;width:131px;height:131px;background:linear-gradient(170deg,#f0f2f3,#c8ced3 55%,#6d7780)"></div>
  <div class="footer"><span>10/10/2023</span><span class="rule"></span><span>06</span></div>
</section>

<!-- 07 Agenda with phones -->
<section class="slide" style="left:31px;top:482px">
  <div class="photo" role="img" aria-label="Business meeting tinted blue" style="left:0;top:0;width:128px;height:208px;background:linear-gradient(160deg,#13a6d8,#0c8cc2 60%,#0a73a6)"></div>
  <div class="title" style="top:12px">AGENDA</div>
  <p class="txt white" style="left:13px;top:36px;width:108px;font-size:4.8px;line-height:1.28">Lorem ipsum dolor sit amet, consectetuer adipiscing elit, sed diam nonummy nibh euismod tincidunt ut laoreet dolore magna aliquam erat volutpat. Ut wisi enim ad minim veniam,</p>
  <p class="txt white" style="left:13px;top:80px;width:108px;font-size:4.8px;line-height:1.28">quis nostrud exerci tation ullam-corper suscipit lobortis nisl ut aliquip ex ea commodo consequat. Duis autem vel eum iriure dolor in hendrerit in vulputate velit esse</p>
  <div class="num sm" style="left:19px;top:120px">1.</div><div class="item-h sm" style="left:34px;top:119px;color:#fff">Lorem ipsum</div><div class="item-p" style="left:34px;top:126px;font-size:2.6px">Lorem ipsum dolor sit amet, consectetuer<br>adipiscing elit, sed diam nonummy nibh</div>
  <div class="num sm" style="left:19px;top:143px">2.</div><div class="item-h sm" style="left:34px;top:142px;color:#fff">Lorem ipsum</div><div class="item-p" style="left:34px;top:149px;font-size:2.6px">Lorem ipsum dolor sit amet, consectetuer<br>adipiscing elit, sed diam nonummy nibh</div>
  <div class="num sm" style="left:19px;top:166px">3.</div><div class="item-h sm" style="left:34px;top:165px;color:#fff">Lorem ipsum</div><div class="item-p" style="left:34px;top:172px;font-size:2.6px">Lorem ipsum dolor sit amet, consectetuer<br>adipiscing elit, sed diam nonummy nibh</div>
  <div class="photo" role="img" aria-label="Faint world map background" style="left:140px;top:55px;width:200px;height:100px;background:radial-gradient(ellipse at center,#eef0f2,#fff 70%)"></div>
  <div class="brand" style="right:12px"><span class="mark"></span><span class="name">StatuteWorks</span><span class="tag">Workplace Policy Advisors</span></div>
  <div class="phone" style="left:153px;top:21px"><h5>Lorem ipsum dolor</h5><svg width="46" height="10" viewBox="0 0 46 10"><rect x="19" y="2" width="8" height="6" fill="none" stroke="var(--orange)" stroke-width=".6"/></svg><p>To introduce the students to the changing landscape of marketing and equip them with knowledge and tools to navigate the digital world.</p></div>
  <div class="phone" style="left:213px;top:51px"><h5>Dolor sit amet, conse</h5><svg width="46" height="12" viewBox="0 0 46 12"><circle cx="23" cy="6" r="4" fill="none" stroke="var(--orange)" stroke-width=".6"/></svg><p>You will learn concepts and ideas in digital marketing as well as how to use different tools and strategies to optimize your digital marketing campaigns.</p></div>
  <div class="phone" style="left:273px;top:84px"><h5>Consec</h5><svg width="46" height="14" viewBox="0 0 46 14"><circle cx="23" cy="8" r="4" fill="none" stroke="var(--orange)" stroke-width=".6"/></svg><p>You are required to pass 80% of the evaluation test to obtain the certificate. The evaluation test can only be taken 3 times.</p></div>
  <div class="footer light"><span>10/10/2023</span><span class="rule" style="margin-left:115px"></span><span style="color:var(--ink)">07</span></div>
</section>

<!-- 08 Text here with tiles -->
<section class="slide" style="left:415px;top:482px">
  <div class="title">TEXT HERE</div>
  <div class="brand"><span class="mark"></span><span class="name">StatuteWorks</span><span class="tag">Workplace Policy Advisors</span></div>
  <p class="txt" style="left:13px;top:35px;width:345px">Lorem ipsum dolor sit amet, consectetuer adipiscing elit, sed diam nonummy nibh euismod tincidunt ut laoreet dolore magna aliquam erat volutpat. Ut wisi enim ad minim veniam, quis nostrud exerci tation ullamcorper suscipit lobortis nisl ut aliquip ex ea commodo consequat. Duis autem vel eum iriure dolor in hendrerit in vulputate velit esse molestie consequat, vel illum dolore eu feugiat nulla facilisis at vero eros et accumsan et iusto odio dignissim qui blandit praesent luptatum zzril delenit augue duis dolore te feugait nulla facilisi.</p>
  <p class="txt" style="left:13px;top:68px;width:345px">Lorem ipsum dolor sit amet, cons ectetuer adipiscing elit, sed diam nonummy nibh euismod tincidunt ut laoreet dolore magna aliquam erat volutpat. Ut wisi enim ad minim veniam, quis nostrud exerci tation ullamcorper suscipit lobortis nisl ut aliquip ex ea commodo consequat.</p>
  <div class="abs" style="left:0;top:117px;width:370px;height:65px;background:var(--blue)"></div>
  <div class="tile" style="left:21px;top:95px"><div class="img" role="img" aria-label="Hand touching a glowing digital interface" style="background:linear-gradient(135deg,#0b2a4a,#3d7fb0 60%,#e9b86b)"></div><h6>Lorem ipsum</h6><p>Lorem ipsum dolor sit amet, consectetuer adipiscing elit, sed diam nonummy nibh euismod tincidunt ut laoreet</p></div>
  <div class="tile" style="left:103px;top:95px"><div class="img" role="img" aria-label="Business people meeting around a table" style="background:linear-gradient(135deg,#e6ebee,#a9b5bf 60%,#4e5b66)"></div><h6>Lorem ipsum</h6><p>Lorem ipsum dolor sit amet, consectetuer adipiscing elit, sed diam nonummy nibh euismod tincidunt ut laoreet</p></div>
  <div class="tile" style="left:185px;top:95px"><div class="img" role="img" aria-label="Finger pressing a blue technology button" style="background:radial-gradient(circle at 55% 50%,#6fd0ff,#1a6fb0 45%,#0b2848)"></div><h6>Lorem ipsum</h6><p>Lorem ipsum dolor sit amet, consectetuer adipiscing elit, sed diam nonummy nibh euismod tincidunt ut laoreet</p></div>
  <div class="tile" style="left:267px;top:95px"><div class="img" role="img" aria-label="Agile process icons on a blue screen" style="background:linear-gradient(135deg,#0e3656,#2b7ea5 55%,#0d3350)"></div><h6>Lorem ipsum</h6><p>Lorem ipsum dolor sit amet, consectetuer adipiscing elit, sed diam nonummy nibh euismod tincidunt ut laoreet</p></div>
  <div class="footer"><span>10/10/2023</span><span class="rule"></span><span>08</span></div>
</section>

<!-- 09 Our company -->
<section class="slide" style="left:799px;top:482px">
  <div class="title" style="top:14px">OUR COMPANY</div>
  <div class="brand"><span class="mark"></span><span class="name">StatuteWorks</span><span class="tag">Workplace Policy Advisors</span></div>
  <div class="abs info" style="left:32px;top:44px;width:168px;height:136px;background:var(--blue);padding:7px 7px">
    <p><b>Lorem ipsum :</b> dolor sit amet, consectetuer adipiscing elit, nonummy nibh euismod tincidunt ut laoreet dolore magna</p>
    <p><b>Lorem ipsum :</b> dolor sit amet, consectetuer adipiscing el sed diam nonummy nibh euismod tincidunt ut laoreet dolore magna aliquam erat volutpat. Ut wisi enim ad minut .</p>
    <p><b>Lorem ipsum :</b> dolor sit amet, consectetuer adipis cing elit, sed diam nonummy nibh euismod tinci dunt ut laoreet magna aliquam erat volutpat.</p>
    <p><b>Lorem ipsum :</b> dolor sit amet, consectetuer adipiscing nibh euismod tincidunt ut laoreet dolore magna</p>
    <p><b>Lorem ipsum :</b> dolor sit amet, consectetuer adipis cing elit, sed diam nonummy nibh euismod tinci dunt ut laoreet magna aliquam erat volutpat.</p>
  </div>
  <div class="abs" style="left:211px;top:47px;font-size:9.5px;font-weight:700;line-height:1.4;color:var(--navy)">WHAT'S A DOMAIN?<br>IT'S THAT NAME UP<br><span style="color:var(--orange);font-weight:900">IN THE ADDRESS BAR.</span></div>
  <ul class="bullets" style="left:217px;top:92px">
    <li>Fits your business or products</li><li>Is easy to spell and remember</li><li>Fits your business or products</li><li>Is easy to spell and remember</li><li>Fits your business or products</li><li>Is easy to spell and remember</li>
  </ul>
  <div class="footer"><span>10/10/2023</span><span class="rule"></span><span>09</span></div>
</section>

<!-- 10 Table -->
<section class="slide" style="left:31px;top:706px">
  <div class="abs" style="left:0;top:0;width:114px;height:4px;background:var(--blue)"></div>
  <div class="abs" style="left:0;top:204px;width:114px;height:4px;background:var(--blue)"></div>
  <div class="title">TEXT HERE</div>
  <div class="brand" style="right:12px"><span class="mark"></span><span class="name">StatuteWorks</span><span class="tag">Workplace Policy Advisors</span></div>
  <div class="num sm" style="left:18px;top:53px">1.</div><div class="item-h sm" style="left:34px;top:52px">Lorem ipsum</div><div class="item-p dark" style="left:34px;top:59px">Lorem ipsum dolor sit amet, consectetuer<br>adipiscing elit, sed diam nonummy nibh</div>
  <div class="num sm" style="left:18px;top:78px">2.</div><div class="item-h sm" style="left:34px;top:77px">Lorem ipsum</div><div class="item-p dark" style="left:34px;top:84px">Lorem ipsum dolor sit amet, consectetuer<br>adipiscing elit, sed diam nonummy nibh</div>
  <div class="num sm" style="left:18px;top:102px">3.</div><div class="item-h sm" style="left:34px;top:101px">Lorem ipsum</div><div class="item-p dark" style="left:34px;top:108px">Lorem ipsum dolor sit amet, consectetuer<br>adipiscing elit, sed diam nonummy nibh</div>
  <div class="num sm" style="left:18px;top:126px">1.</div><div class="item-h sm" style="left:34px;top:125px">Lorem ipsum</div><div class="item-p dark" style="left:34px;top:132px">Lorem ipsum dolor sit amet, consectetuer<br>adipiscing elit, sed diam nonummy nibh</div>
  <div class="num sm" style="left:18px;top:150px">2.</div><div class="item-h sm" style="left:34px;top:149px">Lorem ipsum</div><div class="item-p dark" style="left:34px;top:156px">Lorem ipsum dolor sit amet, consectetuer<br>adipiscing elit, sed diam nonummy nibh</div>
  <table class="table">
    <tr><td style="vertical-align:top;padding-top:3px">Sample Table</td><td></td><td></td></tr>
    <tr><td></td><td></td><td></td></tr>
    <tr><td></td><td></td><td></td></tr>
    <tr><td></td><td></td><td></td></tr>
    <tr><td></td><td></td><td></td></tr>
  </table>
  <div class="footer"><span>10/10/2023</span><span class="rule"></span><span>10</span></div>
</section>

<!-- 11 Team -->
<section class="slide" style="left:415px;top:706px">
  <div class="abs" style="left:0;top:0;width:280px;height:30px;background:var(--blue)"></div>
  <div class="abs" style="left:0;top:30px;width:370px;height:100px;background:var(--blue)"></div>
  <div class="title">TEXT HERE</div>
  <div class="brand"><span class="mark"></span><span class="name">StatuteWorks</span><span class="tag">Workplace Policy Advisors</span></div>
  <p class="txt white" style="left:18px;top:37px;width:245px;font-size:5.8px;line-height:1.25">Lorem ipsum dolor sit amet, consectetuer adipiscing elit, sed diam nonummy nibh euismod tincidunt ut laoreet dolore magna aliquam erat volutpat. Ut wisi enim ad minim veniam, quis nostrud exerci tation ullamcorper suscipit lobortis nisl ut aliquip ex ea commodo consequat. Duis autem</p>
  <p class="txt white" style="left:18px;top:76px;width:245px;font-size:5.8px;line-height:1.25">Lorem ipsum dolor sit amet, cons ectetuer adipiscing elit, sed diam nonummy nibh euismod tincidunt ut laoreet dolore magna aliquam erat volutpat.</p>
  <div class="avatar" role="img" aria-label="Portrait of team member" style="left:28px;top:98px"></div>
  <div class="avatar" role="img" aria-label="Portrait of team member" style="left:126px;top:98px"></div>
  <div class="avatar" role="img" aria-label="Portrait of team member" style="left:222px;top:98px"></div>
  <div class="person" style="left:15px;top:142px"><h6>ALEX MORENO</h6><p>ipsum dolor sit amet, cons ectetuer adipiscing elit, sed diam nonummy nibh euismod tincidunt ut laoreet dolore magna aliquam erat volutpat. Ut wisi enim ad minim veniam, quis nostrud</p></div>
  <div class="person" style="left:113px;top:142px"><h6>DANA REYES</h6><p>ipsum dolor sit amet, cons ectetuer adipiscing elit, sed diam nonummy nibh euismod tincidunt ut laoreet dolore magna aliquam erat volutpat. Ut wisi enim ad minim veniam, quis nostrud</p></div>
  <div class="person" style="left:209px;top:142px"><h6>ALEX MORENO</h6><p>ipsum dolor sit amet, cons ectetuer adipiscing elit, sed diam nonummy nibh euismod tincidunt ut laoreet dolore magna aliquam erat volutpat. Ut wisi enim ad minim veniam, quis nostrud</p></div>
  <div class="abs" style="left:282px;top:117px;width:45px;height:45px;background:var(--peach)"></div>
  <div class="abs" style="left:327px;top:162px;width:43px;height:46px;background:#f0f0f0"></div>
  <div class="footer"><span>10/10/2023</span><span class="rule"></span><span>11</span></div>
</section>

<!-- 12 Thank you -->
<section class="slide" style="left:799px;top:706px">
  <div class="photo" role="img" aria-label="Colleagues talking in a meeting, tinted blue" style="left:0;top:0;width:370px;height:121px;background:linear-gradient(100deg,#0e86bd,#15a9dc 45%,#0e8fc6)"></div>
  <div class="abs" style="left:0;top:58px;width:370px;text-align:center;font-size:27px;font-weight:900;color:#fff;letter-spacing:.5px">THANK YOU</div>
  <div class="abs" style="left:0;top:140px;width:370px;display:flex;justify-content:center;align-items:center;gap:6px">
    <span style="width:12px;height:12px;background:var(--orange)"></span>
    <span style="font-size:18px;font-weight:500;color:var(--navy)">StatuteWorks</span>
  </div>
  <div class="abs" style="left:0;top:164px;width:370px;text-align:center;font-size:5.5px;color:var(--muted)">Workplace Policy Advisors</div>
  <div class="abs" style="left:325px;top:162px;width:23px;height:23px;background:var(--peach)"></div>
  <div class="abs" style="left:348px;top:185px;width:22px;height:23px;background:#f0f0f0"></div>
</section>

</main>
</body>
</html>
```